I need to present the newly formed Cellar Comet concept at a board meeting in 1 weeks time. Cellar Comet is an American gas station Themed dispense concept for wine .. I need a max of 12 page power point template that incorporates a number of the photo elements of the concept and Has the cellar comet logo on each slide .. I have more pics of the concept that I will forward if you accept the project

```html
<!DOCTYPE html>
<html lang="en">
<head>
<meta charset="utf-8">
<title>Cellar Comet – Board Presentation Template</title>
<link href="https://fonts.googleapis.com/css2?family=Poppins:wght@300;400;500;600;700;800&display=swap" rel="stylesheet">
<style>
  :root{
    --board:#c6c6c6;
    --blue:#2f9fde;
    --teal:#35c19c;
    --red:#e2231a;
    --navy:#1d3150;
    --ink:#222;
    --muted:#555;
    --lime:#c5d92f;
    --green:#5db447;
    --deep-green:#1fa384;
    --orange:#f5a21b;
    --col-blue:#2f8fd8;
    --photo-a:#6f7f8c;
    --photo-b:#b9c2b4;
  }
  *{box-sizing:border-box;margin:0;padding:0}
  html,body{width:1200px;height:971px;overflow:hidden}
  body{background:var(--board);font-family:"Poppins",sans-serif;position:relative;color:var(--ink)}
  .slide{position:absolute;width:360px;height:203px;background:#fff;overflow:hidden}
  .abs{position:absolute}
  .shape{position:absolute;left:0;top:0;width:360px;height:203px}
  .logo{position:absolute;font-family:"Poppins",sans-serif;font-weight:700;color:var(--red);font-size:9px;line-height:1;white-space:nowrap}
  .logo.corner{right:14px;text-align:right}
  .logo.chevron{right:8px;text-align:right}
  .photo{position:absolute;background:linear-gradient(135deg,var(--photo-a),var(--photo-b))}
  .photo.pumps{background:linear-gradient(120deg,#3a4f6e 0%,#c9ccb8 45%,#b5342f 70%,#2f6fc0 100%)}
  .photo.people{background:linear-gradient(120deg,#59636b,#a3a9ad 55%,#d6d9da)}
  .tiny{font-size:3.6px;line-height:1.45;color:var(--muted)}
  .small{font-size:5.2px;line-height:1.4;color:var(--ink)}
  .title-white{color:#fff;font-weight:700;line-height:1.05}
  .dots{position:absolute;width:0;border-left:2px dotted var(--red)}

  .s1{left:32px;top:30px}.s2{left:417px;top:30px;width:362px}.s3{left:805px;top:30px}
  .s4{left:32px;top:264px}.s5{left:418px;top:264px}.s6{left:805px;top:264px}
  .s7{left:32px;top:498px}.s8{left:417px;top:498px;width:364px}.s9{left:806px;top:498px}
  .s10{left:32px;top:732px}.s11{left:420px;top:732px}.s12{left:806px;top:732px}

  .agenda-dot{position:absolute;width:32px;height:32px;border-radius:50%;display:flex;align-items:center;justify-content:center}
  .agenda-item h4{font-size:5.6px;font-weight:600;margin-bottom:2px}
  .agenda-item{position:absolute;width:105px}

  .profile{position:absolute;width:65px;height:59px;border:0.8px solid rgba(255,255,255,.9);color:#fff;padding:25px 5px 0}
  .avatar{position:absolute;left:17px;top:-8px;width:30px;height:30px;border-radius:50%;border:1.5px solid #fff;background:linear-gradient(135deg,#8a8f94,#d9d9d9)}
  .profile h5{font-size:5px;font-weight:600}
  .profile .meta{font-size:3.8px;margin-bottom:2px}
  .profile .tiny{color:#fff}

  .service{position:absolute;left:35px;width:100px;text-align:center;color:#fff}
  .service .ic{width:20px;height:20px;border-radius:50%;background:#fff;margin:0 auto 4px;display:flex;align-items:center;justify-content:center}
  .service h5{font-size:4.2px;font-weight:600;color:var(--navy)}
  .service .tiny{color:#eef}

  .plan-col{position:absolute;top:58px;width:75px;height:121px;color:#fff;text-align:center}
  .plan-col .tab{position:absolute;left:8px;top:0;width:59px;height:67px;clip-path:polygon(0 0,100% 0,100% 80%,50% 100%,0 80%);background:linear-gradient(180deg,var(--blue),var(--teal))}
  .plan-col .ico{position:absolute;left:29px;top:26px;width:16px;height:12px}
  .plan-col .pct{position:absolute;left:0;right:0;top:72px;font-size:17px;font-weight:300}
  .plan-col .tiny{position:absolute;left:10px;right:10px;top:98px;color:#fff;text-align:center}

  .step-bar{position:absolute;height:28px;border-radius:9px;background:linear-gradient(90deg,#17324e 0%,#1a5b56 55%,#2bb35c 100%);color:#fff;font-size:15px;font-weight:300;display:flex;align-items:center;justify-content:flex-end;padding-right:8px}
  .step-bar::before{content:"";position:absolute;left:22px;top:11px;border:3px solid transparent;border-right:4px solid #fff}
  .step-label{position:absolute;text-align:right;width:120px}
  .step-label h5{color:var(--red);font-size:5.8px;font-weight:600}
  .step-label .tiny{color:var(--ink)}

  .price-card{position:absolute;text-align:center}
  .price-card .plan{font-size:9px;font-weight:400}
  .price-card .amount{font-size:15px;font-weight:400}
  .price-card .tiny{padding:0 8px}
  .price-card .disc{font-size:5px;font-weight:600;margin-top:5px}
  .btn{position:absolute;left:50%;transform:translateX(-50%);bottom:-4px;font-size:3.6px;font-weight:700;letter-spacing:1px;padding:2px 5px;white-space:nowrap}

  .contact{font-size:5px;line-height:1.3;color:#fff}
  .contact b{font-weight:600}
</style>
</head>
<body>

<svg width="0" height="0" style="position:absolute" aria-hidden="true">
  <defs>
    <linearGradient id="brand" x1="0" y1="0" x2="1" y2="0">
      <stop offset="0" stop-color="#2f9fde"/><stop offset="1" stop-color="#35c19c"/>
    </linearGradient>
    <linearGradient id="brandRev" x1="0" y1="0" x2="1" y2="0">
      <stop offset="0" stop-color="#35c19c"/><stop offset="1" stop-color="#2f9fde"/>
    </linearGradient>
  </defs>
</svg>

<!-- 1 Cover -->
<section class="slide s1">
  <svg class="shape" viewBox="0 0 360 203">
    <polygon points="0,51 44,100 0,149" fill="url(#brand)"/>
    <polygon points="203,0 360,0 360,185 190,185 105,96" fill="url(#brandRev)"/>
  </svg>
  <div class="photo abs" role="img" aria-label="Yellow taxi parked beside a vintage red fuel pump" style="left:43px;top:96px;width:262px;height:60px;background:linear-gradient(90deg,#f4c21c 0%,#e8c94a 45%,#b7b9a6 70%,#d83a2c 100%);border-radius:4px"></div>
  <div class="photo abs" role="img" aria-label="Dark glossy reflective floor" style="left:0;top:155px;width:360px;height:48px;background:linear-gradient(180deg,#3b3f43,#111)"></div>
  <div class="logo" style="left:72px;top:30px;font-size:28px">Cellar Comet</div>
  <div class="abs" style="left:0;right:0;top:176px;text-align:center;color:#fff;font-size:11px;letter-spacing:2px">www.cellarcomet.com</div>
</section>

<!-- 2 Welcome message -->
<section class="slide s2">
  <svg class="shape" viewBox="0 0 362 203" style="width:362px"><rect x="150" y="0" width="212" height="203" fill="url(#brandRev)"/></svg>
  <div class="photo people" role="img" aria-label="Smiling businesswoman gesturing as she speaks" style="left:0;top:0;width:206px;height:203px;clip-path:polygon(0 0,150px 0,206px 100px,150px 203px,0 203px)"></div>
  <div class="abs title-white" style="left:20px;top:88px;font-size:20px;font-weight:600">Welcome</div>
  <div class="abs" style="left:20px;top:110px;font-size:17px;color:var(--red)">Message</div>
  <div class="logo corner" style="top:18px">Cellar Comet</div>
  <div class="abs" style="left:232px;top:58px;font-size:12px;font-weight:500;color:var(--navy)">EVAN HART</div>
  <div class="abs" style="left:232px;top:73px;font-size:4.5px;color:var(--navy)">General Manager</div>
  <p class="abs tiny" style="left:232px;top:90px;width:100px;color:#fff">A short note from our general manager on why the Cellar Comet concept brings the charm of a roadside fuel stop to modern wine service and how we plan to grow it.</p>
</section>

<!-- 3 Agenda -->
<section class="slide s3">
  <div class="photo" role="img" aria-label="Vintage red gas pump" style="left:97px;top:24px;width:56px;height:136px;border-radius:22px 22px 6px 6px;background:linear-gradient(90deg,#9e1610,#e23a2c 50%,#a31812)"></div>
  <svg class="shape" viewBox="0 0 360 203"><polygon points="147,72 265,72 293,105 265,139 147,139" fill="url(#brand)"/></svg>
  <div class="abs title-white" style="left:163px;top:92px;font-size:22px;font-weight:600">Agenda</div>
  <div class="dots" style="left:197px;top:139px;height:64px"></div>
  <div class="logo corner" style="top:18px">Cellar Comet</div>
</section>

<!-- 4 Agenda list -->
<section class="slide s4">
  <div class="dots" style="left:34px;top:0;height:203px"></div>
  <div class="dots" style="left:206px;top:0;height:203px"></div>
  <svg class="shape" viewBox="0 0 360 203"><polygon points="0,60 35,99 0,149" fill="url(#brand)"/></svg>
  <div class="logo corner" style="top:20px">Cellar Comet</div>

  <div class="agenda-dot" style="left:18px;top:52px;background:var(--blue)"><svg width="14" height="12" viewBox="0 0 14 12"><rect x="1" y="4" width="12" height="7" rx="1" fill="#fff"/><rect x="3" y="1" width="8" height="3" fill="#fff"/></svg></div>
  <div class="agenda-dot" style="left:18px;top:96px;background:var(--deep-green)"><svg width="14" height="12" viewBox="0 0 14 12"><circle cx="4" cy="3" r="2" fill="#fff"/><circle cx="10" cy="3" r="2" fill="#fff"/><rect x="2" y="6" width="4" height="6" fill="#fff"/><rect x="8" y="6" width="4" height="6" fill="#fff"/></svg></div>
  <div class="agenda-dot" style="left:18px;top:140px;background:var(--green)"><svg width="14" height="12" viewBox="0 0 14 12"><rect x="1" y="2" width="12" height="9" rx="1" fill="#fff"/></svg></div>
  <div class="agenda-dot" style="left:191px;top:52px;background:var(--orange)"><svg width="10" height="13" viewBox="0 0 10 13"><path d="M5 0 C5 0 0 6 0 8.5 A5 4.5 0 0 0 10 8.5 C10 6 5 0 5 0Z" fill="#fff"/></svg></div>
  <div class="agenda-dot" style="left:191px;top:96px;background:var(--red)"><svg width="10" height="13" viewBox="0 0 10 13"><rect x="1" y="1" width="7" height="11" rx="1" fill="#fff"/><rect x="2.5" y="3" width="4" height="3" fill="var(--red)"/></svg></div>
  <div class="agenda-dot" style="left:191px;top:140px;background:#222"><svg width="16" height="16" viewBox="0 0 16 16"><circle cx="8" cy="8" r="6" fill="none" stroke="#fff" stroke-width="1.3"/><path d="M8 4 V8 L11 10" stroke="#fff" stroke-width="1.3" fill="none"/></svg></div>

  <div class="agenda-item" style="left:58px;top:58px"><h4 style="color:var(--blue)">About the company</h4><p class="tiny">A short summary of this section goes here to guide the board.</p></div>
  <div class="agenda-item" style="left:58px;top:102px"><h4 style="color:var(--deep-green)">Leadership &amp; management Team</h4><p class="tiny">A short summary of this section goes here to guide the board.</p></div>
  <div class="agenda-item" style="left:58px;top:146px"><h4 style="color:var(--green)">Creative Portfolio</h4><p class="tiny">A short summary of this section goes here to guide the board.</p></div>
  <div class="agenda-item" style="left:229px;top:58px"><h4 style="color:var(--orange)">OUR SERVICES</h4><p class="tiny">A short summary of this section goes here to guide the board.</p></div>
  <div class="agenda-item" style="left:229px;top:102px"><h4 style="color:var(--red)">BUSINESS PLAN</h4><p class="tiny">A short summary of this section goes here to guide the board.</p></div>
  <div class="agenda-item" style="left:229px;top:146px"><h4 style="color:#222">TIME LINE</h4><p class="tiny">A short summary of this section goes here to guide the board.</p></div>
</section>

<!-- 5 About the company -->
<section class="slide s5">
  <div class="photo pumps" role="img" aria-label="Two restored vintage fuel pumps in a showroom" style="left:0;top:0;width:360px;height:203px;clip-path:polygon(212px 0,360px 0,360px 203px,265px 203px,172px 100px)"></div>
  <svg class="shape" viewBox="0 0 360 203"><polygon points="360,15 284,100 360,200" fill="url(#brandRev)"/></svg>
  <div class="logo chevron" style="top:96px">Cellar Comet</div>
  <h2 class="abs" style="left:25px;top:20px;font-size:17px;font-weight:700;color:var(--blue);line-height:1.15">About the<br>company</h2>
  <p class="abs small" style="left:25px;top:69px;width:115px">Lorem ipsum dolor sit amet, consectetuer adipiscing elit, sed diam nonummy nibh euismod tincidunt ut laoreet dolore magnaer do consequat. Duis autemlestie.</p>
  <h3 class="abs" style="left:25px;top:112px;font-size:11px;font-weight:600;color:var(--red)">Our Mission</h3>
  <p class="abs small" style="left:25px;top:128px;width:110px">Lorem ipsum dolor sit amet, consectetuer adipiscing elit, sed diam nonummy nibh</p>
  <h3 class="abs" style="left:25px;top:151px;font-size:11px;font-weight:600;color:var(--red)">Our Vision</h3>
  <p class="abs small" style="left:25px;top:167px;width:110px">Lorem ipsum dolor sit amet, consectetuer adipiscing elit, sed diam nonummy nibh</p>
</section>

<!-- 6 Leadership -->
<section class="slide s6">
  <div class="photo people" role="img" aria-label="Two colleagues talking on an office balcony" style="left:0;top:0;width:200px;height:203px"></div>
  <svg class="shape" viewBox="0 0 360 203"><polygon points="171,0 360,0 360,203 171,203 123,100" fill="url(#brandRev)"/></svg>
  <div class="logo corner" style="top:22px">Cellar Comet</div>
  <h2 class="abs title-white" style="left:195px;top:43px;font-size:16px">Leadership &amp;<br>management<br>Team</h2>
  <div class="profile" style="left:195px;top:127px"><div class="avatar" role="img" aria-label="Portrait photo"></div><h5>Marla Quinn</h5><p class="meta">California, 03/14/1990</p><p class="tiny">Short profile text about this team member and their role.</p></div>
  <div class="profile" style="left:273px;top:127px"><div class="avatar" role="img" aria-label="Portrait photo"></div><h5>Marla Quinn</h5><p class="meta">California, 03/14/1990</p><p class="tiny">Short profile text about this team member and their role.</p></div>
</section>

<!-- 7 Creative Portfolio -->
<section class="slide s7">
  <div class="photo pumps" role="img" aria-label="Two restored vintage fuel pumps in a showroom" style="left:0;top:0;width:360px;height:203px;clip-path:polygon(212px 0,360px 0,360px 203px,265px 203px,171px 100px)"></div>
  <svg class="shape" viewBox="0 0 360 203"><polygon points="360,15 284,100 360,200" fill="url(#brandRev)"/></svg>
  <div class="logo chevron" style="top:96px">Cellar Comet</div>
  <h2 class="abs" style="left:33px;top:30px;font-size:16.5px;font-weight:700;color:var(--green);line-height:1.2">Creative<br>Portfolio</h2>
  <p class="abs small" style="left:33px;top:90px;width:118px">Lorem ipsum dolor sit amet, consectetuer adipiscing elit, sed diam nonummy nibh euismod tincidunt ut laoreet dolore magna aliquam erat volutpat. Ut wisi enim ad minim veniam, quis nostrud exerci tation ullamcorper suscipit lobortis nisl ut aliquip ex ea commodo consequat. Duis autem vel eum iriure dolor in hendrerit in vulputate velit esse molestie</p>
</section>

<!-- 8 Our Services -->
<section class="slide s8">
  <div class="photo pumps" role="img" aria-label="Two restored vintage fuel pumps in a showroom" style="left:0;top:0;width:364px;height:203px;clip-path:polygon(190px 0,364px 0,364px 203px,190px 203px)"></div>
  <svg class="shape" viewBox="0 0 364 203" style="width:364px">
    <polygon points="0,0 187,0 211,100 187,203 0,203" fill="url(#brand)"/>
    <polygon points="364,15 290,100 364,200" fill="url(#brandRev)"/>
  </svg>
  <div class="logo chevron" style="top:96px">Cellar Comet</div>
  <h2 class="abs title-white" style="left:25px;top:24px;font-size:16.5px">OUR SERVICES</h2>
  <div class="service" style="top:54px"><div class="ic"><svg width="10" height="8" viewBox="0 0 10 8"><rect x="0" y="2" width="2" height="6" fill="#222"/><rect x="3" y="0" width="2" height="8" fill="#222"/><rect x="6" y="3" width="2" height="5" fill="#222"/></svg></div><h5>Lorem ipsum dolor sit</h5><p class="tiny">A short line about this service offer.</p></div>
  <div class="service" style="top:99px"><div class="ic" style="background:var(--red)"><svg width="10" height="7" viewBox="0 0 10 7"><rect x="0" y="1" width="10" height="5" rx="2.5" fill="#fff"/></svg></div><h5>Lorem ipsum dolor sit</h5><p class="tiny">A short line about this service offer.</p></div>
  <div class="service" style="top:144px"><div class="ic"><svg width="8" height="10" viewBox="0 0 8 10"><rect x="0" y="2" width="8" height="8" rx="1" fill="#222"/><rect x="2" y="0" width="4" height="2" fill="#222"/></svg></div><h5>Lorem ipsum dolor sit</h5><p class="tiny">A short line about this service offer.</p></div>
</section>

<!-- 9 Business Plan -->
<section class="slide s9">
  <svg class="shape" viewBox="0 0 360 203"><polygon points="0,0 211,0 193,50 0,50" fill="url(#brand)"/></svg>
  <h2 class="abs title-white" style="left:23px;top:17px;font-size:16.5px">BUSINESS PLAN</h2>
  <div class="logo corner" style="top:27px">Cellar Comet</div>
  <div class="plan-col" style="left:22px;background:var(--col-blue)"><div class="tab"></div><svg class="ico" viewBox="0 0 16 12"><path d="M1 1 H3 L5 8 H13 L15 3 H4" fill="none" stroke="#fff" stroke-width="1.2"/><circle cx="6" cy="10.5" r="1" fill="#fff"/><circle cx="12" cy="10.5" r="1" fill="#fff"/></svg><div class="pct">75%</div><p class="tiny">A short note about this target.</p></div>
  <div class="plan-col" style="left:102px;background:var(--deep-green)"><div class="tab"></div><svg class="ico" viewBox="0 0 16 12"><rect x="5" y="1" width="6" height="10" rx="2" fill="#fff"/></svg><div class="pct">55%</div><p class="tiny">A short note about this target.</p></div>
  <div class="plan-col" style="left:181px;background:var(--green)"><div class="tab"></div><svg class="ico" viewBox="0 0 16 12"><circle cx="5" cy="6" r="4" fill="none" stroke="#fff"/><rect x="10" y="6" width="1.5" height="5" fill="#fff"/><rect x="13" y="2" width="1.5" height="9" fill="#fff"/></svg><div class="pct">80%</div><p class="tiny">A short note about this target.</p></div>
  <div class="plan-col" style="left:260px;background:var(--orange)"><div class="tab"></div><svg class="ico" viewBox="0 0 16 12"><rect x="1" y="3" width="9" height="6" fill="#fff"/><path d="M10 5 H13 L15 7 V9 H10Z" fill="#fff"/><circle cx="4" cy="10" r="1.2" fill="#fff"/><circle cx="12" cy="10" r="1.2" fill="#fff"/></svg><div class="pct">95%</div><p class="tiny">A short note about this target.</p></div>
</section>

<!-- 10 Time Line -->
<section class="slide s10">
  <svg class="shape" viewBox="0 0 360 203">
    <polygon points="0,0 150,0 175,38 150,76 0,76" fill="url(#brand)"/>
    <polygon points="360,59 331,90 360,123" fill="url(#brandRev)"/>
  </svg>
  <h2 class="abs title-white" style="left:25px;top:31px;font-size:16.5px">TIME LINE</h2>
  <div class="logo corner" style="top:20px">Cellar Comet</div>

  <div class="step-bar" style="left:250px;top:78px;width:70px">40%</div>
  <div class="step-bar" style="left:188px;top:106px;width:93px">30%</div>
  <div class="step-bar" style="left:126px;top:136px;width:92px">20%</div>
  <div class="step-bar" style="left:64px;top:165px;width:93px">10%</div>

  <div class="step-label" style="left:165px;top:55px"><h5>Step Four</h5><p class="tiny">Lorem ipsum dolor sit amet, lacus nulla ac netus<br>nibh aliquet, porttitor ligula justo libero</p></div>
  <div class="step-label" style="left:103px;top:82px"><h5>Step Three</h5><p class="tiny">Lorem ipsum dolor sit amet, lacus nulla ac netus<br>nibh aliquet, porttitor ligula justo libero</p></div>
  <div class="step-label" style="left:41px;top:111px"><h5>Step Two</h5><p class="tiny">Lorem ipsum dolor sit amet, lacus nulla ac netus<br>nibh aliquet, porttitor ligula justo libero</p></div>
  <div class="step-label" style="left:-20px;top:140px"><h5>Step One</h5><p class="tiny">Lorem ipsum dolor sit amet, lacus nulla ac netus<br>nibh aliquet, porttitor ligula justo libero</p></div>
</section>

<!-- 11 Pricing Table -->
<section class="slide s11">
  <svg class="shape" viewBox="0 0 360 203"><polygon points="0,0 211,0 193,50 0,50" fill="url(#brand)"/></svg>
  <h2 class="abs title-white" style="left:26px;top:17px;font-size:16.5px;font-weight:600">Pricing Table</h2>
  <div class="logo corner" style="top:22px">Cellar Comet</div>

  <div class="price-card" style="left:65px;top:68px;width:69px;height:106px;background:var(--lime)">
    <p class="plan" style="margin-top:8px">Regular</p><p class="amount" style="margin-top:4px">$399</p>
    <p class="tiny" style="margin-top:12px;color:#222">Lorem ipsum dolor sit amet, consectetuer adipiscing elit</p><p class="disc">Disc. 25% Off</p>
    <span class="btn" style="background:#222;color:#fff">GET IT NOW</span>
  </div>
  <div class="price-card" style="left:147px;top:58px;width:77px;height:116px;background:#222;color:#fff">
    <p class="plan" style="margin-top:12px">Premium</p><p class="amount" style="margin-top:4px">$479</p>
    <p class="tiny" style="margin-top:12px;color:#ddd">Lorem ipsum dolor sit amet, consectetuer adipiscing elit</p><p class="disc">Disc. 25% Off</p>
    <span class="btn" style="background:var(--lime);color:#fff">GET IT NOW</span>
  </div>
  <div class="price-card" style="left:237px;top:70px;width:69px;height:104px;background:var(--lime)">
    <div style="background:var(--red);color:#fff;height:33px;padding-top:11px" class="plan">Diesel</div><p class="amount" style="margin-top:5px">$529</p>
    <p class="tiny" style="margin-top:9px;color:#222">Lorem ipsum dolor sit amet, consectetuer adipiscing elit</p><p class="disc">Disc. 25% Off</p>
    <span class="btn" style="background:#222;color:#fff">GET IT NOW</span>
  </div>
</section>

<!-- 12 Thank You -->
<section class="slide s12">
  <div class="photo pumps" role="img" aria-label="Two restored vintage fuel pumps in a showroom" style="left:0;top:0;width:360px;height:203px;clip-path:polygon(190px 0,360px 0,360px 203px,190px 203px)"></div>
  <svg class="shape" viewBox="0 0 360 203">
    <polygon points="0,0 193,0 215,100 193,203 0,203" fill="url(#brand)"/>
    <polygon points="360,15 286,100 360,200" fill="url(#brandRev)"/>
  </svg>
  <div class="logo chevron" style="top:96px">Cellar Comet</div>
  <h2 class="abs title-white" style="left:25px;top:88px;font-size:16.5px">THANK YOU</h2>
  <div class="abs" style="left:27px;top:122px;font-size:12px;color:#fff">www.cellarcomet.com</div>
  <div class="abs contact" style="left:29px;top:142px"><b>Telephone :</b><br>+1 555-014-2290 / +1 555-014-7781</div>
  <div class="abs contact" style="left:29px;top:158px"><b>Email :</b><br>hello@cellarcomet.com</div>
  <div class="abs contact" style="left:29px;top:174px"><b>Address :</b><br>Business Name, Street Name 123, 000 City Name</div>
</section>

</body>
</html>
```